Carradine Advisory Cover 1 - Hunting Profit As Moggle Hunts the Flimbit

Carradine Advisory is a business consulting firm. We will publish a series of four thought leadership pieces online and via PDF. The first of the series is attached to this project. We need an eye-catching cover page with a back page that keeps with our branding. The document attached is in the final draft, and the cover and pack pages are placeholders only. You can find more about our branding and style on our website www.carradineadvisory.com.au. The other three projects can be found here with a similar brief, and you are welcome to submit a design for all 4.

```html
<!DOCTYPE html>
<html lang="en">
<head>
<meta charset="utf-8">
<title>Carradine Advisory – Hunting Profit As Moggle Hunts the Flimbit</title>
<link rel="stylesheet" href="https://fonts.googleapis.com/css2?family=Poppins:wght@400;500;600;700&display=swap">
<style>
  :root {
    --ink: #343c48;
    --orange: #f7931e;
    --blue: #1ba1e6;
    --paper: #eef0f3;
    --white: #ffffff;
    --stage: #ffffff;
  }
  * { margin: 0; padding: 0; box-sizing: border-box; }
  html, body { width: 1200px; height: 830px; overflow: hidden; background: var(--stage); }
  body { font-family: "Poppins", Arial, sans-serif; position: relative; }

  .page { position: absolute; top: 0; width: 586px; height: 830px; overflow: hidden; }
  .page--cover { left: 0; background: var(--paper); }
  .page--back { left: 614px; background: var(--ink); }
  .page__art { position: absolute; inset: 0; width: 586px; height: 830px; display: block; }

  .brand { position: absolute; display: flex; align-items: center; gap: 10px; }
  .brand__dot { border-radius: 50%; background: var(--orange); flex: none; }
  .brand__name { font-weight: 600; line-height: 1.05; }
  .page--cover .brand { left: 42px; top: 56px; }
  .page--cover .brand__dot { width: 30px; height: 30px; }
  .page--cover .brand__name { font-size: 18px; color: var(--ink); }
  .page--back .brand { left: 42px; top: 36px; }
  .page--back .brand__dot { width: 44px; height: 44px; }
  .page--back .brand__name { font-size: 30px; color: var(--white); }

  .cover-title { position: absolute; left: 42px; top: 218px; color: var(--white); }
  .cover-title__lead { display: block; font-size: 53px; font-weight: 700; color: var(--orange); line-height: 1.1; margin-bottom: 10px; }
  .cover-title__rest { display: block; font-size: 33px; font-weight: 600; line-height: 1.5; }

  .site { position: absolute; bottom: 28px; display: flex; align-items: center; gap: 6px; color: var(--white); font-size: 14px; font-weight: 500; }
  .page--cover .site { left: 282px; }
  .page--back .site { left: 300px; }
  .site svg { width: 13px; height: 13px; }

  .contact { position: absolute; left: 42px; top: 172px; width: 420px; color: var(--white); }
  .contact__heading { font-size: 35px; font-weight: 600; color: var(--orange); line-height: 1.2; margin-bottom: 26px; }
  .contact__intro { font-size: 21px; font-weight: 500; line-height: 1.3; margin-bottom: 36px; }
  .contact__intro strong { font-weight: 700; }
  .person { margin-bottom: 40px; }
  .person__name { font-size: 21px; font-weight: 600; color: var(--orange); line-height: 1.2; }
  .person__role { font-size: 12px; font-weight: 600; color: var(--blue); line-height: 1.2; margin-bottom: 12px; }
  .person__line { font-size: 13px; line-height: 1.35; }

  .follow { position: absolute; left: 42px; bottom: 28px; display: flex; align-items: center; gap: 12px; color: var(--white); font-size: 12px; font-weight: 600; }
  .follow__mark { width: 13px; height: 13px; background: var(--white); border-radius: 2px; }
</style>
</head>
<body>

<section class="page page--cover">
  <svg class="page__art" viewBox="0 0 420 595" preserveAspectRatio="none" aria-hidden="false">
    <defs>
      <linearGradient id="g-city" x1="0" y1="0" x2="1" y2="1">
        <stop offset="0" stop-color="#5b6f86"/><stop offset="1" stop-color="#a7b3c1"/>
      </linearGradient>
      <linearGradient id="g-stone" x1="0" y1="0" x2="1" y2="1">
        <stop offset="0" stop-color="#c98a3a"/><stop offset="1" stop-color="#e2a658"/>
      </linearGradient>
      <linearGradient id="g-towers" x1="0" y1="0" x2="0" y2="1">
        <stop offset="0" stop-color="#2f8fd0"/><stop offset="1" stop-color="#1b5f93"/>
      </linearGradient>
      <linearGradient id="g-stairs" x1="0" y1="0" x2="1" y2="1">
        <stop offset="0" stop-color="#a8783f"/><stop offset="1" stop-color="#3b6f9c"/>
      </linearGradient>
      <linearGradient id="g-wall" x1="0" y1="0" x2="1" y2="1">
        <stop offset="0" stop-color="#3aa7e4"/><stop offset="1" stop-color="#1f6fa8"/>
      </linearGradient>
    </defs>
    <polygon points="147,130 212,0 230,0 165,130" fill="var(--blue)"/>
    <polygon role="img" aria-label="Photo of a glass office tower" points="169,130 234,0 330,0 265,130" fill="url(#g-city)"/>
    <polygon role="img" aria-label="Photo of textured stone in warm orange tones" points="275,130 340,0 420,0 420,130" fill="url(#g-stone)"/>

    <polygon role="img" aria-label="Photo of a tall blue-toned wall" points="300,130 420,130 420,595 143,595 308,300 300,300" fill="url(#g-wall)"/>
    <polygon role="img" aria-label="Photo of city skyscrapers in blue" points="0,300 292,300 127,595 0,595" fill="url(#g-towers)"/>
    <polygon points="0,300 38,300 0,368" fill="var(--orange)"/>
    <polygon role="img" aria-label="Photo of a figure on a wide stone staircase" points="308,300 415,300 250,595 143,595" fill="url(#g-stairs)"/>
    <polygon points="292,300 308,300 143,595 127,595" fill="var(--white)"/>
    <polygon points="415,300 420,300 420,295 258,595 250,595" fill="var(--white)"/>
    <polygon points="335,595 420,595 420,445" fill="var(--orange)"/>

    <polygon points="0,130 395,130 300,300 0,300" fill="var(--ink)"/>
    <polygon points="395,130 405,130 310,300 300,300" fill="var(--white)"/>
  </svg>

  <div class="brand">
    <span class="brand__dot"></span>
    <span class="brand__name">Carradine<br>Advisory</span>
  </div>

  <h1 class="cover-title">
    <span class="cover-title__lead">Hunting Profit</span>
    <span class="cover-title__rest">As Moggle Hunts<br>the Flimbit</span>
  </h1>

  <div class="site">
    <svg viewBox="0 0 14 14" aria-hidden="true"><circle cx="7" cy="7" r="6" fill="none" stroke="#fff" stroke-width="1.4"/><ellipse cx="7" cy="7" rx="2.6" ry="6" fill="none" stroke="#fff" stroke-width="1.2"/><line x1="1" y1="7" x2="13" y2="7" stroke="#fff" stroke-width="1.2"/></svg>
    <span>www.carradineadvisory.com.au</span>
  </div>
</section>

<section class="page page--back">
  <svg class="page__art" viewBox="0 0 420 595" preserveAspectRatio="none" aria-hidden="true">
    <polygon points="148,595 420,118 420,126 158,595" fill="var(--white)"/>
    <polygon points="160,595 420,138 420,595" fill="var(--blue)"/>
    <polygon points="292,92 316,48 420,48 420,92" fill="var(--blue)"/>
    <polygon points="312,80 334,38 420,38 420,80" fill="var(--orange)"/>
  </svg>

  <div class="brand">
    <span class="brand__dot"></span>
    <span class="brand__name">Carradine<br>Advisory</span>
  </div>

  <div class="contact">
    <h2 class="contact__heading">Contact us</h2>
    <p class="contact__intro">Find out how <strong>Carradine Advisory</strong> can help build your company into a market leader today.</p>

    <div class="person">
      <p class="person__name">Hugo Carradine</p>
      <p class="person__role">Managing Director</p>
      <p class="person__line">Mobile: +61 400 118 236</p>
      <p class="person__line">Email: hugo@carradineadvisory.com.au</p>
    </div>

    <div class="person">
      <p class="person__name">Miles Carradine</p>
      <p class="person__role">Managing Director</p>
      <p class="person__line">Mobile: +61 400 264 901</p>
      <p class="person__line">Email: miles@carradineadvisory.com.au</p>
    </div>
  </div>

  <div class="follow">
    <span>Follow us</span>
    <span class="follow__mark"></span>
    <span class="follow__mark"></span>
  </div>

  <div class="site">
    <svg viewBox="0 0 14 14" aria-hidden="true"><circle cx="7" cy="7" r="6" fill="none" stroke="#fff" stroke-width="1.4"/><ellipse cx="7" cy="7" rx="2.6" ry="6" fill="none" stroke="#fff" stroke-width="1.2"/><line x1="1" y1="7" x2="13" y2="7" stroke="#fff" stroke-width="1.2"/></svg>
    <span>www.carradineadvisory.com.au</span>
  </div>
</section>

</body>
</html>
```